Brindle Yard Care. The best in the biz

I run a lawn care service that offers full service mowing. 100% satisfaction guarantee. Fast, Friendly, quality service "I am your lawns best friend" I cut residential lawns. I offer a mow package that includes trimming, edging and clean up. Prices very from 20 dollars to 75. I want my logo to stand out. Free estimates

Target Market(s)

Home owners

Industry/Entity Type

Landscaping

Contact Information for Business Card

482-615-0273 tomkerl47@quillmail.net Dorian. Brindle Yard care

Colors
f37122
9bcb3c
cadf82

Requirements
Must have
• Company name.
• Phone number
• Email
• My services
• images
Nice to have
• A sun that is growing grass.
Should not have
• Incorrect information

```html
<!DOCTYPE html>
<html lang="en">
<head>
<meta charset="utf-8">
<title>Brindle Yard Care – Business Card</title>
<link rel="stylesheet" href="https://fonts.googleapis.com/css2?family=Open+Sans:wght@400;600;700&display=swap">
<style>
  :root {
    --orange: #f37122;
    --green: #9bcb3c;
    --green-light: #cadf82;
    --green-deep: #2f9a3e;
    --ink: #1f1f1f;
    --card: #ffffff;
    --stage: #e9e6e0;
  }
  * { box-sizing: border-box; margin: 0; padding: 0; }
  html, body { width: 1200px; height: 780px; overflow: hidden; }
  body {
    background: var(--stage);
    font-family: "Open Sans", Arial, sans-serif;
    display: flex;
    align-items: center;
    justify-content: center;
    gap: 40px;
  }
  .card {
    width: 540px;
    height: 309px;
    background: var(--card);
    position: relative;
    overflow: hidden;
    box-shadow: 0 6px 18px rgba(0,0,0,.18);
  }

  /* front */
  .brand {
    position: absolute;
    left: 28px;
    top: 58px;
    width: 200px;
  }
  .brand-name {
    color: var(--green-deep);
    font-weight: 700;
    font-size: 26px;
    line-height: 1.15;
  }
  .contact {
    position: absolute;
    right: 28px;
    top: 50px;
    width: 280px;
    text-align: right;
  }
  .contact-name { color: var(--green); font-weight: 700; font-size: 28px; line-height: 1.1; }
  .contact-business { color: var(--orange); font-size: 18px; margin-bottom: 10px; }
  .contact-line {
    color: var(--ink);
    font-size: 17px;
    display: flex;
    align-items: center;
    justify-content: flex-end;
    gap: 8px;
    line-height: 1.55;
    white-space: nowrap;
  }
  .contact-icon { width: 18px; height: 18px; flex: none; }
  .promise {
    position: absolute;
    right: 28px;
    bottom: 30px;
    text-align: right;
    color: var(--orange);
    font-size: 17px;
    line-height: 1.35;
  }

  /* back */
  .card-back svg { display: block; }
</style>
</head>
<body>

<section class="card card-front">
  <div class="brand">
    <p class="brand-name">Fernwick Grounds</p>
  </div>

  <div class="contact">
    <p class="contact-name">Dorian</p>
    <p class="contact-business">Brindle Yard care</p>
    <p class="contact-line">482-615-0273
      <svg class="contact-icon" viewBox="0 0 18 18" aria-hidden="true">
        <rect width="18" height="18" fill="var(--orange)"/>
        <path d="M5 4h2.5l1 3-1.5 1a7 7 0 0 0 3 3l1-1.5 3 1V13a1 1 0 0 1-1 1A9 9 0 0 1 4 5a1 1 0 0 1 1-1z" fill="#fff"/>
      </svg>
    </p>
    <p class="contact-line">tomkerl47@quillmail.net
      <svg class="contact-icon" viewBox="0 0 18 18" aria-hidden="true">
        <rect width="18" height="18" fill="var(--orange)"/>
        <rect x="3.5" y="5" width="11" height="8" fill="none" stroke="#fff" stroke-width="1.3"/>
        <path d="M3.5 5l5.5 4.5L14.5 5" fill="none" stroke="#fff" stroke-width="1.3"/>
      </svg>
    </p>
  </div>

  <div class="promise">
    <p>100% satisfaction guarantee</p>
    <p>Fast, Friendly, quality service</p>
  </div>
</section>

<section class="card card-back">
  <svg width="540" height="309" viewBox="0 0 540 309">
    <defs>
      <linearGradient id="gardenTones" x1="0" y1="0" x2="1" y2="1">
        <stop offset="0" stop-color="#8d8e9a"/>
        <stop offset=".35" stop-color="#6fae3a"/>
        <stop offset=".7" stop-color="#4f9a2c"/>
        <stop offset="1" stop-color="#9a9bab"/>
      </linearGradient>
    </defs>
    <rect width="540" height="309" fill="url(#gardenTones)" role="img" aria-label="Photo of a landscaped rock garden with clipped round shrubs and grey boulders"/>
    <path d="M150 309 C 260 250, 330 170, 540 150 L540 309 Z" fill="#ffffff"/>
    <path d="M150 309 C 260 250, 330 170, 540 150" fill="none" stroke="var(--green)" stroke-width="7"/>
    <path d="M170 309 C 275 258, 345 182, 540 164" fill="none" stroke="var(--green-light)" stroke-width="3"/>
  </svg>
</section>

</body>
</html>
```